Tarvel Ridge LLC

Need Professional Business cards for New Investment Fund

Target Market(s)

High Quality investors

Industry/Entity Type

Financial

Contact Information for Business Card

Phone Number +1 555 284 6193
Name Pavel Orlinsky
Title Fund Manager
email po@FundTarvel.example
Website www.FundTarvel.example

Colors

Designer to choose colors to be used in the design.

Requirements
Must have
• Must have our Logo and all of the above. Must be made so lettering and loge can be raised

```html
<!DOCTYPE html>
<html lang="en">
<head>
<meta charset="utf-8">
<title>Tarvel Ridge LLC – Business Card</title>
<link href="https://fonts.googleapis.com/css2?family=Jost:wght@500&family=Roboto:wght@400;700&display=swap" rel="stylesheet">
<style>
  :root {
    --backdrop: #a8a8a8;
    --card-dark: #3a443b;
    --card-light: #f2f2f1;
    --mark-on-dark: #9aa39b;
    --ink-dark: #3a443b;
    --ink-text: #333a35;
    --accent: #7cb518;
  }
  html, body {
    margin: 0;
    padding: 0;
    width: 1200px;
    height: 1138px;
    overflow: hidden;
    background: var(--backdrop);
  }
  .card {
    position: absolute;
    left: 274px;
    width: 622px;
    height: 374px;
    border-radius: 16px;
    overflow: hidden;
  }
  .card--front {
    top: 186px;
    background: var(--card-dark);
  }
  .card--back {
    top: 608px;
    background: var(--card-light);
  }
  .wordmark {
    position: absolute;
    left: 0;
    right: 0;
    text-align: center;
    font-family: "Jost", sans-serif;
    font-weight: 500;
    text-transform: uppercase;
    letter-spacing: 1px;
    white-space: nowrap;
  }
  .card--front .wordmark {
    top: 154px;
    font-size: 56px;
    line-height: 1;
    color: var(--mark-on-dark);
  }
  .card--back .wordmark {
    top: 72px;
    font-size: 50px;
    line-height: 1;
    color: var(--ink-dark);
  }
  .holder {
    position: absolute;
    left: 0;
    right: 0;
    text-align: center;
    font-family: "Roboto", sans-serif;
  }
  .holder__name {
    top: 211px;
    font-size: 22px;
    font-weight: 700;
    letter-spacing: 0.5px;
    color: var(--accent);
    text-transform: uppercase;
  }
  .holder__title {
    top: 241px;
    font-size: 15px;
    color: var(--ink-text);
  }
  .contact {
    position: absolute;
    left: 0;
    right: 0;
    display: flex;
    justify-content: center;
    gap: 18px;
    font-family: "Roboto", sans-serif;
    font-size: 15.5px;
    color: var(--ink-text);
  }
  .contact--phone { top: 280px; }
  .contact--web { top: 304px; }
  .contact__item {
    display: flex;
    align-items: center;
    gap: 10px;
  }
  .contact__icon {
    width: 13px;
    height: 13px;
    fill: var(--accent);
  }
  .band {
    position: absolute;
    left: 0;
    right: 0;
    bottom: 0;
    height: 16px;
    background: linear-gradient(90deg, var(--ink-dark) 0%, var(--ink-dark) 15%, var(--accent) 85%);
  }
</style>
</head>
<body>
  <section class="card card--front" aria-label="Card front">
    <div class="wordmark">Tarvel Ridge</div>
  </section>

  <section class="card card--back" aria-label="Card back">
    <div class="wordmark">Tarvel Ridge</div>

    <div class="holder holder__name">Pavel Orlinsky</div>
    <div class="holder holder__title">Fund Manager</div>

    <div class="contact contact--phone">
      <span class="contact__item">
        <svg class="contact__icon" viewBox="0 0 16 16" aria-hidden="true"><path d="M2 4c0-1.5 2.5-2.5 6-2.5S14 2.5 14 4v1.5h-3V4H5v1.5H2zM4 7h8l2 6H2z"/></svg>
        +1 555 284 6193
      </span>
    </div>

    <div class="contact contact--web">
      <span class="contact__item">
        <svg class="contact__icon" viewBox="0 0 16 16" aria-hidden="true"><path d="M1 3h14v1L8 9 1 4zM1 5.5l7 5 7-5V13H1z"/></svg>
        po@FundTarvel.example
      </span>
      <span class="contact__item">
        <svg class="contact__icon" viewBox="0 0 16 16" aria-hidden="true"><path d="M8 1a7 7 0 1 0 0 14A7 7 0 0 0 8 1zm0 1.5c.8 0 1.7 1.6 2 4H6c.3-2.4 1.2-4 2-4zM2.6 6.5h2.1a12 12 0 0 0 0 3H2.6a5.5 5.5 0 0 1 0-3zm3.4 3h4c-.3 2.4-1.2 4-2 4s-1.7-1.6-2-4zm5.3 0a12 12 0 0 0 0-3h2.1a5.5 5.5 0 0 1 0 3z"/></svg>
        www.FundTarvel.example
      </span>
    </div>

    <div class="band"></div>
  </section>
</body>
</html>
```